Design business card for new business which advocates for elders in nursing homes or personal care h

New business for rights of the elderly residents who reside in personal care homes and or nursing homes. I am looking for a business card with logo of keystone for Pennsylvania and something in side the keystone that represents healthcare, advocates, something on that line; monitor care received and needs of resident. Chart audits, State Regulation compliance

Target Market(s)

Seniors no longer safe to live at home by themselves along with their kids

Industry/Entity Type

Business

Contact Information for Business Card

Keystone symbol to represent Pensylvaoa with some kind of symbol inside to represent advocate, seniors, or healthcare symbol

Font styles to use
Serif

Colors
33a6d7
85cae6
abd037

Requirements
Must have
• Brightwell Elder Allies is our business name; our tag line is Path to Better Living
Nice to have
• Nice logo

```html
<!DOCTYPE html>
<html lang="en">
<head>
<meta charset="utf-8">
<title>Brightwell Elder Allies — Business Card</title>
<link rel="stylesheet" href="https://fonts.googleapis.com/css2?family=Cormorant+Garamond:wght@600&family=Roboto:wght@400;700&display=swap">
<style>
  :root {
    --sky: #85cae6;
    --ocean: #33a6d7;
    --lime: #abd037;
    --ink: #3a3a3a;
    --paper: #ffffff;
    --backdrop: #e6e6e6;
  }
  * { margin: 0; padding: 0; box-sizing: border-box; }
  html, body { width: 1200px; height: 1187px; overflow: hidden; background: var(--backdrop); }
  .sheet {
    position: relative; width: 1200px; height: 1187px;
    display: flex; align-items: center; justify-content: center; gap: 30px;
  }
  .card {
    position: relative; width: 560px; height: 311px;
    background: var(--paper); overflow: hidden;
    box-shadow: 0 2px 6px rgba(0,0,0,.18);
  }
  .card-art { position: absolute; inset: 0; width: 100%; height: 100%; }

  /* contact side */
  .contact { position: absolute; left: 233px; top: 28px; font-family: "Roboto", Arial, sans-serif; color: var(--ink); }
  .contact-name { font-weight: 700; font-size: 22px; color: var(--ocean); line-height: 26px; }
  .contact-role { font-size: 17px; line-height: 22px; margin-bottom: 20px; }
  .contact-address { font-size: 17px; line-height: 24px; margin-bottom: 18px; }
  .contact-lines { list-style: none; font-size: 17px; line-height: 24px; }
  .contact-lines li { display: flex; align-items: center; gap: 6px; }
  .contact-icon { width: 14px; height: 14px; flex: none; }

  /* brand side */
  .brand { background: var(--sky); }
  .brand-dot { position: absolute; left: 249px; top: 67px; width: 62px; height: 62px; border-radius: 50%; background: var(--ocean); }
  .brand-text { position: absolute; left: 0; right: 0; top: 160px; text-align: center; font-family: "Cormorant Garamond", Georgia, serif; font-weight: 600; color: var(--ink); }
  .brand-name { font-size: 33px; line-height: 38px; letter-spacing: .5px; }
  .brand-tagline { font-size: 31px; line-height: 40px; }
</style>
</head>
<body>
<main class="sheet">

  <section class="card contact-card">
    <svg class="card-art" viewBox="0 0 510 283" preserveAspectRatio="none" aria-hidden="true">
      <polygon fill="#abd037" points="0,20 122,20 104,75 156,75 94,274 0,274"/>
      <polygon fill="#85cae6" points="0,31 107,31 89,86 140,86 85,263 0,263"/>
    </svg>
    <div class="contact">
      <p class="contact-name">YOUR NAME</p>
      <p class="contact-role">ADVOCATE</p>
      <p class="contact-address">Your Address Line -1<br>Your Address line &amp; Pincod<br>Place, 1237667,Cw aaa<br>Country</p>
      <ul class="contact-lines">
        <li>
          <svg class="contact-icon" viewBox="0 0 14 14" aria-hidden="true"><rect width="14" height="14" rx="3" fill="#33a6d7"/><path d="M4 3.2l1.6 0 .7 2-1 .8a6 6 0 0 0 2.7 2.7l.8-1 2 .7v1.6c-4 .6-7.4-2.8-6.8-6.8z" fill="#fff"/></svg>
          555 014 2087
        </li>
        <li>
          <svg class="contact-icon" viewBox="0 0 14 14" aria-hidden="true"><rect width="14" height="14" rx="3" fill="#33a6d7"/><rect x="3" y="4" width="8" height="6" fill="#fff"/><path d="M3 4l4 3.2L11 4" stroke="#33a6d7" stroke-width="1" fill="none"/></svg>
          hello@brightwellallies.com
        </li>
        <li>
          <svg class="contact-icon" viewBox="0 0 14 14" aria-hidden="true"><rect width="14" height="14" rx="3" fill="#33a6d7"/><circle cx="7" cy="7" r="4" stroke="#fff" stroke-width="1" fill="none"/><path d="M3 7h8M7 3c-2 2.5-2 5.5 0 8M7 3c2 2.5 2 5.5 0 8" stroke="#fff" stroke-width=".8" fill="none"/></svg>
          www.brightwellallies.com
        </li>
      </ul>
    </div>
  </section>

  <section class="card brand">
    <svg class="card-art" viewBox="0 0 510 283" preserveAspectRatio="none" aria-hidden="true">
      <polygon fill="#abd037" points="78,28 432,28 410,116 492,116 468,283 42,283 18,116 100,116"/>
      <polygon fill="#ffffff" points="100,50 410,50 388,138 468,138 448,283 62,283 42,138 122,138"/>
    </svg>
    <span class="brand-dot"></span>
    <div class="brand-text">
      <p class="brand-name">BRIGHTWELL<br>ELDER ALLIES</p>
      <p class="brand-tagline">Path to Better Living</p>
    </div>
  </section>

</main>
</body>
</html>
```